This is a label for a new sake made in Japan imported into Aust

This will be a bottle label for a new sake imported into Australia. The hero of the label is the Velmora. We have joined the "O" meaning great in Japanese and used sake with "Z" to have Velmora with the play on words using Oz as in our slang for Aussie. A modern label with a Japanese take is key. This is a premium sake made in Japan for the Australian market.
The "Tall Casks" up the top is the name of the company, we have yet to design a logo for the company.

Target Market(s)

Alcohol

Logo Text

Velmora

Font styles to use
Serif

Requirements
Must have
• easy to read, with a hint of Japanese origin
Should not have
• too busy

```html
<!DOCTYPE html>
<html lang="en">
<head>
<meta charset="utf-8">
<title>Velmora – Premium Japanese Sake Labels</title>
<link rel="stylesheet" href="https://fonts.googleapis.com/css2?family=Poiret+One&family=Playfair+Display:wght@400;700&family=Montserrat:wght@600&display=swap">
<style>
  :root {
    --page: #f1f1f1;
    --paper: #fbfbfb;
    --ink: #1b1b1b;
    --ink-soft: #2a2a2a;
    --ink-light: #f4f4f4;
    --red: #b3202b;
    --red-deep: #9c1a24;
    --band-dark: #262626;
    --band-light: #ececec;
    --band-text-dark: #9a9a9a;
    --band-text-light: #c4c4c4;
  }
  * { box-sizing: border-box; margin: 0; padding: 0; }
  html, body {
    width: 1200px;
    height: 1100px;
    overflow: hidden;
    background: var(--page);
  }
  .canvas {
    width: 1200px;
    height: 1100px;
    display: flex;
    align-items: center;
    justify-content: center;
    gap: 90px;
  }
  .label {
    position: relative;
    width: 500px;
    height: 540px;
    display: flex;
    flex-direction: column;
    box-shadow: 0 2px 10px rgba(0,0,0,0.08);
  }
  .label__body {
    position: relative;
    flex: 1;
  }
  .label--light .label__body { background: var(--paper); color: var(--ink); }
  .label--dark .label__body { background: var(--ink-soft); color: var(--ink-light); }

  .company {
    position: absolute;
    top: 52px;
    left: 0;
    width: 430px;
    text-align: center;
    font-family: "Poiret One", sans-serif;
    font-size: 40px;
    letter-spacing: 1px;
    line-height: 1;
  }

  .spec-box {
    position: absolute;
    top: 34px;
    right: 18px;
    width: 64px;
    height: 200px;
    background: var(--red);
    padding: 6px;
  }
  .spec-box__inner {
    width: 100%;
    height: 100%;
    background: #fff;
    border: 1.5px solid var(--red-deep);
    display: flex;
    flex-direction: column;
    justify-content: space-around;
    align-items: center;
    font-family: "Playfair Display", serif;
    font-size: 14px;
    color: #444;
    text-align: center;
    line-height: 1.4;
  }
  .spec-box__divider {
    width: 80%;
    border-top: 1px dotted #777;
  }

  .brand-name {
    position: absolute;
    left: 0;
    right: 0;
    top: 300px;
    text-align: center;
    font-family: "Playfair Display", serif;
    font-weight: 700;
    font-size: 78px;
    letter-spacing: 3px;
    line-height: 1;
  }

  .label__band {
    height: 56px;
    display: flex;
    align-items: center;
    justify-content: center;
    font-family: "Montserrat", sans-serif;
    font-weight: 600;
    font-size: 19px;
    letter-spacing: 3px;
  }
  .label--light .label__band { background: var(--band-dark); color: var(--band-text-dark); }
  .label--dark .label__band { background: var(--band-light); color: var(--band-text-light); }
</style>
</head>
<body>
<main class="canvas">

  <section class="label label--light">
    <div class="label__body">
      <p class="company">TALL CASKS</p>
      <div class="spec-box">
        <div class="spec-box__inner">
          <span>ALC<br>16%</span>
          <span class="spec-box__divider"></span>
          <span>VOL<br>720 ml</span>
        </div>
      </div>
      <p class="brand-name">VELMORA</p>
    </div>
    <div class="label__band">PREMIUM JAPANESSE SAKE</div>
  </section>

  <section class="label label--dark">
    <div class="label__body">
      <p class="company">TALL CASKS</p>
      <div class="spec-box">
        <div class="spec-box__inner">
          <span>ALC<br>16%</span>
          <span class="spec-box__divider"></span>
          <span>VOL<br>720 ml</span>
        </div>
      </div>
      <p class="brand-name">VELMORA</p>
    </div>
    <div class="label__band">PREMIUM JAPANESSE SAKE</div>
  </section>

</main>
</body>
</html>
```